依頼詳細
法人向け新サービスのダイレクトメール(はがきサイズ)を制作しますので、オフセット印刷入稿用デザインをお願い致します。

表は宛名印刷用ですので、下4分の一程度のデザイン(単色1c)、裏は全面デザイン(4c)をお願いします。

アウトドア用品の会社ですが、今回は法人向けDMですので、目を引くデザインを求めます。

・テンプレート(win・mac)用添付いたします。
・テキストは添付のとおりですが、デザイン・文字級数含め、レイアウトなどは、自由にご提案ください。
・写真画像は添付しますが、カンプ用のダミーですので、発注者が決まり次第、本番用の写真をお渡しします。
記載項目
テキストは添付ファイルの通りです。
希望イメージ
シンプル 複雑
単色 カラフル
暗い 明るい
日常 高級
遊び心 厳粛
未来的 伝統的
女性的 男性的
希望する色
水色系、茶系、緑系、黄・オレンジ系、色味などは弊社HPなども参考にしてください。さわやかな青系なども可です。
納品ファイル
• 高解像度JPG (.jpg)
• イラストレーター形式 (.ai)
補足説明
■ 選んだ理由

法人向けという堅い部分とアウトドア用品という柔らかさのバランス、見出しや文字級数の強弱のつけ方、DMという特性上、ぱっと見で入ってくる印象などで決定させていただきました。

■ 提案者全員のお礼・コメント

沢山のご提案ありがとうございました。
皆様それぞれに良い部分がありましたが、上記の部分を踏まえて、決定させていただきました。
またご機会がありましたら、何卒宜しくお願い申し上げます。

```html
<!DOCTYPE html>
<html lang="ja">
<head>
<meta charset="utf-8">
<title>こもれびの森 はがき宛名面</title>
<link rel="stylesheet" href="https://fonts.googleapis.com/css2?family=Noto+Sans+JP:wght@400;500;700;900&family=Noto+Serif+JP:wght@500&display=swap">
<style>
  :root {
    --paper: #ffffff;
    --ink: #2b2b2b;
    --ink-soft: #6a6a6a;
    --bubble: #e4e4e4;
    --line: #444444;
  }
  * { margin: 0; padding: 0; box-sizing: border-box; }
  html, body { width: 809px; height: 1200px; overflow: hidden; background: var(--paper); }
  .postcard {
    position: relative; width: 809px; height: 1200px; background: var(--paper);
    font-family: "Noto Sans JP", sans-serif; color: var(--ink);
  }
  .postcard-label {
    position: absolute; top: 30px; left: 0; width: 100%; text-align: center;
    font-family: "Noto Serif JP", serif; font-size: 20px; letter-spacing: 2px; color: var(--ink-soft);
  }
  .postage-mark { position: absolute; left: 36px; top: 16px; }
  .postage-mark text { font-family: "Noto Serif JP", serif; fill: var(--ink-soft); font-size: 28px; letter-spacing: 6px; }

  .brand-name {
    position: absolute; left: 40px; top: 1008px; width: 275px;
    font-size: 42px; font-weight: 900; line-height: 56px; white-space: nowrap; text-align: center;
  }
  .search-box {
    position: absolute; left: 40px; top: 1080px; width: 275px; height: 36px;
    display: flex; border: 2px solid var(--ink);
    font-size: 18px; font-weight: 700; white-space: nowrap;
  }
  .search-term { flex: 1; display: flex; align-items: center; padding-left: 10px; }
  .search-action { display: flex; align-items: center; padding: 0 10px; background: var(--ink); color: var(--paper); }
  .brand-url {
    position: absolute; left: 40px; top: 1124px; width: 275px;
    font-size: 18px; line-height: 26px; letter-spacing: .5px; white-space: nowrap;
  }

  .contact-bubble { position: absolute; left: 490px; top: 895px; }
  .contact-bubble-text {
    position: absolute; left: 490px; top: 895px; width: 282px; height: 56px; line-height: 56px;
    text-align: center; font-size: 18px; font-weight: 500; white-space: nowrap;
  }
  .contact-tel {
    position: absolute; right: 38px; top: 960px;
    font-size: 40px; font-weight: 900; letter-spacing: 1px; line-height: 50px; white-space: nowrap;
  }
  .contact-address {
    position: absolute; right: 38px; top: 1018px;
    font-size: 17px; font-weight: 500; line-height: 24px; white-space: nowrap;
  }
  .contact-mail {
    position: absolute; right: 38px; top: 1050px;
    font-size: 19px; line-height: 26px; display: flex; align-items: center; gap: 10px; white-space: nowrap;
  }
</style>
</head>
<body>
<main class="postcard">
  <p class="postcard-label">郵便はがき</p>

  <svg class="postage-mark" width="180" height="180" viewBox="0 0 180 180" aria-label="料金別納郵便">
    <circle cx="88" cy="88" r="84" fill="none" stroke="var(--line)" stroke-width="2"/>
    <line x1="6" y1="98" x2="170" y2="98" stroke="var(--line)" stroke-width="2"/>
    <text x="88" y="84" text-anchor="middle">料金別納</text>
    <text x="88" y="136" text-anchor="middle">郵　便</text>
  </svg>

  <section class="brand">
    <p class="brand-name">こもれびの森</p>
    <div class="search-box">
      <span class="search-term">こもれびの森</span>
      <span class="search-action">で検索!</span>
    </div>
    <p class="brand-url">http://komorebi-mori.net</p>
  </section>

  <section class="contact">
    <svg class="contact-bubble" width="282" height="66" viewBox="0 0 282 66" aria-hidden="true">
      <path d="M28 1 H254 A27 27 0 0 1 254 55 H56 L40 65 L42 55 H28 A27 27 0 0 1 28 1 Z" fill="var(--bubble)"/>
    </svg>
    <span class="contact-bubble-text">お問い合わせはお気軽に!</span>
    <p class="contact-tel">tel.0555-00-1234</p>
    <p class="contact-address">〒400-0000 山梨県甲府市北町1-2-3</p>
    <p class="contact-mail">
      <svg width="24" height="18" viewBox="0 0 24 18" aria-hidden="true">
        <rect x="1" y="1" width="22" height="16" fill="none" stroke="var(--ink)" stroke-width="1.6"/>
        <polyline points="1,1 12,10 23,1" fill="none" stroke="var(--ink)" stroke-width="1.6"/>
      </svg>
      <span>info@komorebi-mori.net</span>
    </p>
  </section>
</main>
</body>
</html>
```